STOREFRONT SIGNAGE/ NEW LOGO

Looking for someone to enhance my current sign idea. I own a pawn shop , which is also a gun shop. I want a catchy front sign, which will be a lighted box sign. I may want to incorporate some symbols or character symbology that highlight firearms, such as : guns, ammo, targets, scope retical , gold, diamonds, cash, watches and/or pawn balls, and im open to other ideas, but i do not want it too busy, i want it simple, with a twist. Attached, you will find a very basic design, showing the business name and the verbiage that I would like to be incorporated into the design. God bless and thank you. may the best design win !

```html
<!DOCTYPE html>
<html lang="en">
<head>
<meta charset="UTF-8">
<title>Gold &amp; Gun Exchange Sign</title>
<link rel="stylesheet" href="https://fonts.googleapis.com/css2?family=Poppins:wght@700;800&family=Roboto:wght@900&display=swap">
<style>
  :root {
    --page-bg: #dedede;
    --sign-black: #000000;
    --sign-white: #ffffff;
    --gold-dark: #8a6a1f;
    --gold-mid: #c9a045;
    --gold-light: #f3dc96;
    --red: #e00000;
    --silver-light: #ffffff;
    --silver-dark: #8d8d8d;
    --ink: #111111;
  }
  * { margin: 0; padding: 0; box-sizing: border-box; }
  html, body { width: 960px; height: 1200px; overflow: hidden; }
  body { background: var(--page-bg); position: relative; }

  .sign {
    position: absolute; left: 30px; top: 469px;
    width: 900px; height: 262px;
    background: var(--sign-black);
    box-shadow: 0 10px 24px rgba(0,0,0,.35);
    overflow: hidden;
  }
  .sign__bands { position: absolute; left: 0; top: 0; }

  .brand-mark {
    position: absolute; left: 59px; top: 28px;
    width: 120px; height: 120px; border-radius: 50%;
    background: var(--gold-mid);
  }
  .brand-name {
    position: absolute; left: 40px; top: 155px; width: 158px;
    text-align: center;
    font: 700 20px/1 'Poppins', sans-serif; letter-spacing: 1px;
    color: var(--gold-mid);
  }

  .headline {
    position: absolute; top: 8px;
    font: 800 94px/1 'Poppins', sans-serif; letter-spacing: -2px;
  }
  .headline--gold {
    left: 220px;
    background: linear-gradient(90deg, var(--gold-dark), var(--gold-light) 50%, var(--gold-mid));
    -webkit-background-clip: text; background-clip: text; color: transparent;
  }
  .headline--gun { right: 44px; color: var(--red); }

  .exchange {
    position: absolute; top: 99px;
    font: 900 42px/1 'Roboto', sans-serif; color: var(--sign-white);
  }
  .exchange--gold { left: 223px; }
  .exchange--gun { right: 44px; }

  .ampersand {
    position: absolute; left: 494px; top: 39px;
    width: 98px; height: 98px; border-radius: 50%;
    background: radial-gradient(circle at 35% 30%, var(--silver-light), #d4d4d4 45%, var(--silver-dark));
    display: flex; align-items: center; justify-content: center;
    font: 800 66px/1 'Poppins', sans-serif; color: var(--ink);
    padding-top: 6px;
  }

  .tagline {
    position: absolute; top: 155px;
    font: 800 24px/1 'Poppins', sans-serif; color: var(--ink);
  }
  .tagline--gold { left: 255px; }
  .tagline--gun { right: 44px; }

  .services {
    position: absolute; left: 0; top: 194px; width: 900px; height: 68px;
    background: var(--sign-white);
  }
  .service {
    position: absolute; top: 16px;
    display: flex; align-items: center; gap: 7px;
    font: 900 35px/1 'Roboto', sans-serif; color: var(--ink);
  }
  .service svg { width: 24px; height: 24px; flex: none; }
</style>
</head>
<body>
  <div class="sign">
    <svg class="sign__bands" width="900" height="194" viewBox="0 0 900 194">
      <defs>
        <linearGradient id="goldBand" x1="0" y1="0" x2="1" y2="0">
          <stop offset="0" stop-color="#8a6a1f"/>
          <stop offset="0.55" stop-color="#f3dc96"/>
          <stop offset="1" stop-color="#c9a045"/>
        </linearGradient>
      </defs>
      <polygon points="230,148 545,148 523,189 207,189" fill="url(#goldBand)"/>
      <polygon points="552,148 900,148 900,189 530,189" fill="#e00000"/>
    </svg>

    <div class="brand-mark"></div>
    <div class="brand-name">MERIDIAN</div>

    <div class="headline headline--gold">GOLD</div>
    <div class="exchange exchange--gold">EXCHANGE</div>

    <div class="ampersand">&amp;</div>

    <div class="headline headline--gun">GUN</div>
    <div class="exchange exchange--gun">EXCHANGE</div>

    <div class="tagline tagline--gold">CASH FOR GOLD</div>
    <div class="tagline tagline--gun">CASH FOR GUNS</div>

    <div class="services">
      <div class="service" style="left:47px"><svg viewBox="0 0 24 24"><circle cx="12" cy="12" r="12" fill="#e00000"/><path d="M6.5 12.5l3.6 3.6 7.4-7.6" fill="none" stroke="#fff" stroke-width="2.6" stroke-linecap="round" stroke-linejoin="round"/></svg>PAWN</div>
      <div class="service" style="left:214px"><svg viewBox="0 0 24 24"><circle cx="12" cy="12" r="12" fill="#e00000"/><path d="M6.5 12.5l3.6 3.6 7.4-7.6" fill="none" stroke="#fff" stroke-width="2.6" stroke-linecap="round" stroke-linejoin="round"/></svg>BUY</div>
      <div class="service" style="left:343px"><svg viewBox="0 0 24 24"><circle cx="12" cy="12" r="12" fill="#e00000"/><path d="M6.5 12.5l3.6 3.6 7.4-7.6" fill="none" stroke="#fff" stroke-width="2.6" stroke-linecap="round" stroke-linejoin="round"/></svg>SELL</div>
      <div class="service" style="left:476px"><svg viewBox="0 0 24 24"><circle cx="12" cy="12" r="12" fill="#e00000"/><path d="M6.5 12.5l3.6 3.6 7.4-7.6" fill="none" stroke="#fff" stroke-width="2.6" stroke-linecap="round" stroke-linejoin="round"/></svg>TRADE</div>
      <div class="service" style="left:641px"><svg viewBox="0 0 24 24"><circle cx="12" cy="12" r="12" fill="#e00000"/><path d="M6.5 12.5l3.6 3.6 7.4-7.6" fill="none" stroke="#fff" stroke-width="2.6" stroke-linecap="round" stroke-linejoin="round"/></svg>LAYAWAY</div>
    </div>
  </div>
</body>
</html>
```